ORBIT conference Slide Deck

This is a conference for our team that will be 3 days of discussions on how to build our business in the middle of these challenging time. Its a bit of a battle and so we are going with a red and grey/black these although I am open to your interpretation. I will include a few graphics that we have started on to show you the look. But I am just getting started, INSPIRE ME! The screen will be 100' across the front of the room and these decks will show on each side and I will reformat for the middle 1X6 screen as needed. I have the AI file of the logo if you need it. I don't see where to upload it here.

Target Market(s)

our top producers

Industry/Entity Type

Real Estate Agent

Font styles to use
Sans Serif

Colors
ec1f27

Requirements
Must have
• Depth, creativity

```html
<!DOCTYPE html>
<html lang="en">
<head>
<meta charset="utf-8">
<title>ORBIT Company Meeting — Slide Deck</title>
<link rel="stylesheet" href="https://fonts.googleapis.com/css2?family=Noto+Sans:wght@400;500&display=swap">
<style>
  :root {
    --canvas: #ffffff;
    --slide-bg: #f6f5f3;
    --card-bg: #ffffff;
    --ink: #111111;
    --ink-soft: #2a2a2a;
    --muted: #6b7888;
    --accent: #ec1f27;
    --number: #e8642a;
    --photo-light: #d9d9d9;
    --photo-dark: #5a5a5a;
  }
  * { margin: 0; padding: 0; box-sizing: border-box; }
  html, body { width: 1200px; height: 675px; overflow: hidden; background: var(--canvas); }
  body { position: relative; font-family: "Noto Sans", Arial, sans-serif; color: var(--ink); }

  .slide { position: absolute; width: 595px; height: 333px; background: var(--slide-bg); overflow: hidden; }
  .slide--agenda { left: 3px; top: 3px; }
  .slide--productivity { left: 602px; top: 3px; }
  .slide--checklist { left: 3px; top: 339px; }
  .slide--practices { left: 602px; top: 339px; }

  .menu-icon { position: absolute; right: 33px; top: 34px; width: 12px; height: 12px; }

  .slide-number { position: absolute; left: 33px; top: 288px; font-size: 9px; color: var(--muted); letter-spacing: 0.5px; }
  .slide-footer { position: absolute; right: 34px; top: 290px; font-size: 6.8px; letter-spacing: 1.3px; color: var(--muted); }

  /* Agenda */
  .agenda-title { position: absolute; left: 49px; top: 60px; font-size: 32px; font-weight: 400; letter-spacing: -0.3px; }
  .agenda-dot { position: absolute; left: 81px; top: 130px; width: 11px; height: 11px; border-radius: 50%; background: var(--accent); }
  .agenda-lead { position: absolute; left: 107px; top: 124px; font-size: 13.5px; }
  .agenda-list { position: absolute; left: 107px; top: 164px; list-style: none; font-size: 12.5px; line-height: 15.7px; letter-spacing: 0.3px; color: var(--ink-soft); }
  .agenda-list li::before { content: "— "; }

  /* Productivity */
  .feature-photo { position: absolute; left: 86px; top: 58px; width: 153px; height: 214px; background: linear-gradient(160deg, var(--photo-light) 0%, #a8a8a8 45%, var(--photo-dark) 100%); }
  .feature-dot { position: absolute; left: 67px; top: 89px; width: 39px; height: 39px; border-radius: 50%; background: var(--accent); }
  .feature-title { position: absolute; left: 277px; top: 74px; font-size: 31px; font-weight: 400; line-height: 35px; }
  .feature-subtitle { position: absolute; left: 277px; top: 170px; font-size: 10.8px; }
  .feature-body { position: absolute; left: 277px; top: 202px; width: 265px; font-size: 7px; line-height: 11.9px; color: var(--ink-soft); }

  /* Cards */
  .section-title { position: absolute; left: 0; right: 0; text-align: center; font-weight: 400; }
  .slide--checklist .section-title { top: 48px; font-size: 32px; }
  .slide--practices .section-title { top: 50px; font-size: 20.5px; }

  .card { position: absolute; width: 150px; background: var(--card-bg); border-radius: 10px; }
  .slide--checklist .card { top: 122px; height: 164px; }
  .slide--practices .card { top: 106px; height: 165px; }
  .card--1 { left: 49px; } .card--2 { left: 224px; } .card--3 { left: 400px; }
  .slide--practices .card--1 { left: 47px; } .slide--practices .card--2 { left: 222px; } .slide--practices .card--3 { left: 398px; }

  .card-tick { position: absolute; left: 13px; top: 12px; width: 12px; height: 10px; }
  .card-number { position: absolute; left: 13px; top: 10px; font-size: 15px; color: var(--number); }
  .card-label { position: absolute; left: 13px; top: 55px; font-size: 8.8px; line-height: 12.5px; color: var(--muted); }
  .card-body { position: absolute; left: 13px; top: 78px; font-size: 7px; line-height: 12px; color: var(--ink-soft); }
  .slide--practices .card-body--low { top: 91px; }
</style>
</head>
<body>

<svg width="0" height="0" style="position:absolute">
  <defs>
    <symbol id="menu" viewBox="0 0 12 12"><rect y="0.5" width="12" height="1.8" fill="#ec1f27"/><rect y="5.1" width="12" height="1.8" fill="#ec1f27"/><rect y="9.7" width="12" height="1.8" fill="#ec1f27"/></symbol>
    <symbol id="tick" viewBox="0 0 12 10"><path d="M1 5.2 L4.4 8.4 L11 1.4" fill="none" stroke="#ec1f27" stroke-width="2.2" stroke-linecap="round" stroke-linejoin="round"/></symbol>
  </defs>
</svg>

<section class="slide slide--agenda">
  <svg class="menu-icon"><use href="#menu"/></svg>
  <h1 class="agenda-title">Key Talking Points</h1>
  <span class="agenda-dot"></span>
  <p class="agenda-lead">What's on the agenda?</p>
  <ul class="agenda-list">
    <li>Work-from-home best practices</li>
    <li>In-progress projects</li>
    <li>Project roadblocks</li>
    <li>First quarter wins</li>
    <li>Things to keep in mind</li>
  </ul>
  <span class="slide-number">02.</span>
  <span class="slide-footer">ORBIT COMPANY MEETING | JUNE 2020</span>
</section>

<section class="slide slide--productivity">
  <svg class="menu-icon"><use href="#menu"/></svg>
  <div class="feature-photo" role="img" aria-label="Black and white photo of three colleagues reviewing plans and a tablet at a desk"></div>
  <span class="feature-dot"></span>
  <h1 class="feature-title">Managing<br>productivity</h1>
  <p class="feature-subtitle">Working efficiently in challenging times</p>
  <p class="feature-body">To create a stunning presentation, it's best to simplify your thoughts. Start with an outline of topics and identify highlights, which can be applied to whatever subject you plan on discussing. You can then organize them into your introduction, your main content, and your conclusion.</p>
  <span class="slide-number">03.</span>
  <span class="slide-footer">ORBIT COMPANY MEETING | JUNE 2020</span>
</section>

<section class="slide slide--checklist">
  <svg class="menu-icon"><use href="#menu"/></svg>
  <h1 class="section-title">Remote work checklist</h1>
  <article class="card card--1">
    <svg class="card-tick"><use href="#tick"/></svg>
    <h2 class="card-label">Stable internet connection</h2>
    <p class="card-body">To create a stunning presentation,<br>it's best to simplify your thoughts.<br>Start with an outline of topics and<br>identify highlights, which can be<br>applied to whatever subject you<br>plan on discussing.</p>
  </article>
  <article class="card card--2">
    <svg class="card-tick"><use href="#tick"/></svg>
    <h2 class="card-label">Desktop or laptop</h2>
    <p class="card-body">Make sure you do enough research<br>to support your points. It's also a<br>good idea to pair data with visual<br>aids like charts or images. It all<br>depends on the purpose of your<br>presentation.</p>
  </article>
  <article class="card card--3">
    <svg class="card-tick"><use href="#tick"/></svg>
    <h2 class="card-label">Noise-cancelling headset</h2>
    <p class="card-body">Remember to keep your<br>presentation easy-to-read. Avoid<br>overloading a slide with too many<br>words and choose a color palette<br>that won't distract the audience.</p>
  </article>
</section>

<section class="slide slide--practices">
  <svg class="menu-icon"><use href="#menu"/></svg>
  <h1 class="section-title">Work-from-home best practices</h1>
  <article class="card card--1">
    <span class="card-number">1</span>
    <h2 class="card-label">Stick to a schedule.</h2>
    <p class="card-body">To create a stunning presentation,<br>it's best to simplify your thoughts.<br>Start with an outline of topics and<br>identify highlights, which can be<br>applied to whatever subject you<br>plan on discussing.</p>
  </article>
  <article class="card card--2">
    <span class="card-number">2</span>
    <h2 class="card-label">Document progress<br>and actions taken.</h2>
    <p class="card-body card-body--low">Make sure you do enough research<br>to support your points. It's also a<br>good idea to pair data with visual<br>aids like charts or images. It all<br>depends on the purpose.</p>
  </article>
  <article class="card card--3">
    <span class="card-number">3</span>
    <h2 class="card-label">Do your best to be responsive.</h2>
    <p class="card-body">Remember to keep your<br>presentation easy-to-read. Avoid<br>overloading a slide with too many<br>words and choose a color palette<br>that won't distract the audience.</p>
  </article>
  <span class="slide-number">05.</span>
  <span class="slide-footer">ORBIT COMPANY MEETING | JUNE 2020</span>
</section>

</body>
</html>
```